Commercial Construction Company

We need a business card design based on our current logo. We are a commercial general contractor based in Southern California that specializes in bank remodels. We would like to see designs that incorporate dark blue. The final design should portray an image of professionalism and quality.

If possible, I would like to add metallic foil to the design. Thank you

```html
<!DOCTYPE html>
<html lang="en">
<head>
<meta charset="utf-8">
<title>Halden Commercial Builders – Business Card</title>
<link href="https://fonts.googleapis.com/css2?family=Poppins:wght@400;500;600;700&display=swap" rel="stylesheet">
<style>
  :root {
    --stage: #2b2b2e;
    --navy-light: #3a3488;
    --navy-dark: #1b1850;
    --brand-blue: #1d4f8c;
    --steel-grey: #a7a9ad;
    --ink: #111111;
    --muted: #9a9a9a;
    --paper: #ffffff;
  }
  * { box-sizing: border-box; margin: 0; padding: 0; }
  html, body { width: 1200px; height: 880px; overflow: hidden; }
  body {
    background: var(--stage);
    font-family: "Poppins", sans-serif;
    position: relative;
  }
  .card {
    position: absolute;
    left: 300px;
    width: 600px;
    height: 343px;
    border-radius: 18px;
    overflow: hidden;
  }
  /* Back side */
  .card-back {
    top: 70px;
    background: linear-gradient(135deg, var(--navy-light) 0%, var(--navy-dark) 60%);
    color: var(--paper);
  }
  .card-back .wordmark {
    position: absolute;
    top: 120px;
    left: 0; right: 0;
    display: flex;
    align-items: center;
    justify-content: center;
    gap: 14px;
  }
  .wordmark-dot {
    width: 22px; height: 22px;
    border-radius: 50%;
    background: var(--brand-blue);
  }
  .wordmark-name {
    font-weight: 700;
    font-size: 30px;
    letter-spacing: 1px;
    line-height: 1.1;
  }
  .card-back .address {
    position: absolute;
    bottom: 40px;
    left: 0; right: 0;
    text-align: center;
    font-size: 13px;
    font-weight: 400;
    letter-spacing: 0.2px;
  }
  /* Front side */
  .card-front {
    top: 467px;
    background: var(--paper);
  }
  .card-front .swoosh {
    position: absolute;
    inset: 0;
  }
  .card-front .wordmark {
    position: absolute;
    top: 96px;
    left: 40px;
    width: 230px;
    display: flex;
    align-items: center;
    gap: 10px;
    color: var(--ink);
  }
  .card-front .wordmark-name { font-size: 26px; }
  .divider {
    position: absolute;
    left: 288px;
    top: 64px;
    width: 1px;
    height: 120px;
    background: var(--brand-blue);
  }
  .contact {
    position: absolute;
    left: 310px;
    top: 56px;
  }
  .contact .name {
    font-size: 17px;
    font-weight: 600;
    color: var(--ink);
    line-height: 1.2;
  }
  .contact .title {
    font-size: 12px;
    color: var(--muted);
    margin-bottom: 10px;
  }
  .contact ul { list-style: none; }
  .contact li {
    display: flex;
    align-items: center;
    gap: 8px;
    font-size: 12.5px;
    color: var(--ink);
    line-height: 1.6;
  }
  .contact li svg { width: 14px; height: 14px; flex: none; }
</style>
</head>
<body>

  <section class="card card-back" aria-label="Business card, back">
    <div class="wordmark">
      <span class="wordmark-dot"></span>
      <span class="wordmark-name">Halden Commercial Builders</span>
    </div>
    <p class="address">118 Larkspur Street, Suite 210, Fairview, CA 92001</p>
  </section>

  <section class="card card-front" aria-label="Business card, front">
    <svg class="swoosh" viewBox="0 0 600 343" preserveAspectRatio="none" aria-hidden="true">
      <path d="M0 300 C 60 330, 120 343, 160 343 L0 343 Z" fill="var(--steel-grey)"/>
      <path d="M0 292 C 220 300, 420 250, 575 110 L 590 122 C 440 275, 230 318, 0 306 Z" fill="var(--brand-blue)"/>
    </svg>

    <div class="wordmark">
      <span class="wordmark-dot"></span>
      <span class="wordmark-name">HALDEN</span>
    </div>

    <div class="divider"></div>

    <div class="contact">
      <p class="name">Your name here</p>
      <p class="title">Managing Director</p>
      <ul>
        <li>
          <svg viewBox="0 0 14 14"><circle cx="7" cy="7" r="7" fill="var(--brand-blue)"/><path d="M4.5 3.8l1.3 1.3-.7 1c.5 1 1.2 1.7 2.2 2.2l1-.7 1.3 1.3-.8 1C6.5 9.7 4.3 7.5 3.6 4.6z" fill="#fff"/></svg>
          555-014-2735
        </li>
        <li>
          <svg viewBox="0 0 14 14"><circle cx="7" cy="7" r="7" fill="var(--brand-blue)"/><rect x="5" y="3.3" width="4" height="7.4" rx="0.8" fill="none" stroke="#fff" stroke-width="1"/></svg>
          555-016-1234
        </li>
        <li>
          <svg viewBox="0 0 14 14"><circle cx="7" cy="7" r="7" fill="var(--brand-blue)"/><rect x="3.6" y="4.6" width="6.8" height="4.8" fill="none" stroke="#fff" stroke-width="1"/><path d="M3.6 4.6L7 7.4l3.4-2.8" fill="none" stroke="#fff" stroke-width="1"/></svg>
          yourname@haldencb.com
        </li>
        <li>
          <svg viewBox="0 0 14 14"><circle cx="7" cy="7" r="7" fill="var(--brand-blue)"/><circle cx="7" cy="7" r="3.6" fill="none" stroke="#fff" stroke-width="0.9"/><path d="M3.4 7h7.2M7 3.4c-1.6 2-1.6 5.2 0 7.2M7 3.4c1.6 2 1.6 5.2 0 7.2" fill="none" stroke="#fff" stroke-width="0.8"/></svg>
          www.haldencb.com
        </li>
      </ul>
    </div>
  </section>

</body>
</html>
```